Group training gym/bootcamp needs a web design

We need a website for our gym that is based in Sydney. We have indoor functional training classes and outdoor bootcamp classes. We would like the web site to have a video (to be created) and photo gallery. I would like the site made on word press and i would like to be able to make minor changes such as changing images and text without having to use a designer.

The website should have the following pages: home page; the gym; the bootcamp; photo gallery; about us; contact.

I have uploaded our logo and i would like to keep to these colour (blue,yellow,silver) and black is also allowed

Target Market(s)

18-50 male and female

Industry/Entity Type

Gym

Coding

Coded - Design and coding required

Number of Pages Required

5+ page

Font styles to use
Sans Serif

Colors
0692cd
fbed22
1b1b1b
e8e8e8

Requirements
Must have
• The website should have the following pages: home page; the gym; the bootcamp; photo gallery; about us; contact.
• I have uploaded our logo and i would like to keep to these colour (blue,yellow,silver) and black is also allowed
• Video upload and photo upload

```html
<!DOCTYPE html>
<html lang="en">
<head>
<meta charset="utf-8">
<title>Ironbark Training Hub</title>
<link href="https://fonts.googleapis.com/css2?family=Open+Sans:wght@400;600;700&family=Source+Sans+3:wght@400;700&family=Syncopate:wght@700&display=swap" rel="stylesheet">
<style>
:root{
  --blue:#0a77c4;
  --blue-light:#2a8fd6;
  --yellow:#e2b806;
  --yellow-panel:rgba(150,118,0,.78);
  --ink:#1b1b1b;
  --grey:#8a8a8a;
  --silver:#e8e8e8;
  --white:#ffffff;
}
*{margin:0;padding:0;box-sizing:border-box}
html,body{width:1107px;height:1200px;overflow:hidden;background:var(--white)}
body{position:relative;font-family:"Open Sans",sans-serif;color:var(--ink)}
.abs{position:absolute}

/* header */
.brand{left:73px;top:44px;display:flex;align-items:center;gap:10px;font-family:"Open Sans",sans-serif;font-weight:700;font-size:17px;color:var(--blue);letter-spacing:.5px}
.brand-dot{width:26px;height:26px;border-radius:50%;background:var(--yellow)}
.contact-bar{right:74px;top:26px;display:flex;align-items:center;font-size:14px;color:var(--grey)}
.contact-item{display:flex;align-items:center;gap:8px}
.contact-sep{width:1px;height:26px;background:var(--silver);margin:0 18px}
.nav{right:30px;top:74px;display:flex;gap:0;list-style:none}
.nav li{font-size:14.5px;color:var(--yellow);margin-left:41px}
.nav li.active{color:var(--blue-light)}

/* hero */
.hero{left:0;top:120px;width:1107px;height:769px;background:
  radial-gradient(ellipse at 48% 35%,rgba(120,80,50,.55),transparent 55%),
  radial-gradient(ellipse at 55% 90%,rgba(70,70,70,.6),transparent 60%),
  linear-gradient(180deg,#1b2a30 0%,#20262a 45%,#141618 100%)}
.hero-title{left:0;width:1107px;top:190px;text-align:center;font-family:"Syncopate",sans-serif;font-weight:700;font-size:40px;color:var(--white);letter-spacing:1px}
.hero-sub{left:0;width:1107px;top:251px;text-align:center;font-size:15.5px;letter-spacing:3.2px;color:var(--white)}
.card{top:338px;width:289px}
.card-photo{height:192px;width:100%}
.card-photo.framed{border:1px solid var(--white)}
.card-body{margin-top:10px;height:192px;background:var(--yellow-panel);position:relative;text-align:center;padding-top:32px}
.card-body::before{content:"";position:absolute;left:50%;top:-18px;margin-left:-18px;border:18px solid transparent;border-top:0;border-bottom-color:var(--yellow-panel)}
.card-title{font-family:"Source Sans 3",sans-serif;font-weight:700;font-size:23px;color:var(--ink);letter-spacing:.3px}
.card-text{margin:18px auto 0;width:235px;font-size:14px;line-height:21px;color:var(--ink)}
.plus{left:109px;top:63px}
.arrows{left:520px;top:803px;display:flex;gap:11px}

/* footer */
.f-head{top:937px;font-family:"Source Sans 3",sans-serif;font-size:21px;color:var(--blue);letter-spacing:.4px}
.links{top:977px;left:73px;display:grid;grid-template-columns:125px 120px;row-gap:8px;list-style:none;font-size:14px;color:var(--grey)}
.links li.active{color:var(--yellow)}
.touch-text{left:388px;top:977px;width:300px;font-size:14px;line-height:20px;color:var(--grey)}
.email-box{left:386px;top:1029px;width:241px;height:34px;border:1px solid #cfcfcf;display:flex;align-items:center;justify-content:space-between;padding:0 14px 0 9px;font-size:14px;color:var(--grey);letter-spacing:.5px}
.loc{left:775px;top:977px;font-size:14px;color:var(--grey)}
.loc-row{display:flex;margin-bottom:14px;line-height:20px}
.loc-label{width:63px;font-size:12.5px;color:var(--ink)}
.divider{left:0;top:1128px;width:1107px;height:1px;background:var(--silver)}
.copyright{left:73px;top:1155px;font-size:14px;color:var(--ink)}
.copyright b{color:var(--yellow);font-size:12.5px;letter-spacing:.8px}
.social{right:50px;top:1148px;display:flex;gap:6px}
.social span{width:33px;height:33px;border:1px solid #d9d9d9}
.social span.on{border:2px solid var(--yellow)}
</style>
</head>
<body>

<header>
  <div class="abs brand"><span class="brand-dot"></span>IRONBARK TRAINING HUB</div>
  <div class="abs contact-bar">
    <span class="contact-item">
      <svg width="20" height="20" viewBox="0 0 24 24" fill="none" stroke="#0a77c4" stroke-width="1.6"><path d="M5 3l4 1 1 5-2 1.5a11 11 0 0 0 5.5 5.5L15 14l5 1 1 4-2 2C10 21 3 14 3 5z"/></svg>
      123 555 0190
    </span>
    <span class="contact-sep"></span>
    <span class="contact-item">
      <svg width="20" height="20" viewBox="0 0 24 24" fill="none" stroke="#0a77c4" stroke-width="1.6"><path d="M22 2L2 10l8 3 3 8z M10 13L22 2"/></svg>
      hello@ironbarktraininghub.com
    </span>
  </div>
  <ul class="abs nav">
    <li class="active">HOME</li><li>THE GYM</li><li>THE BOOTCAMP</li><li>GALLERY</li><li>ABOUT US</li><li>CONTACT</li>
  </ul>
</header>

<section class="abs hero" role="img" aria-label="Athlete lifting weights in a gym with a rack of dumbbells in the foreground"></section>
<h1 class="abs hero-title">IRONBARK TRAINING HUB</h1>
<p class="abs hero-sub">PUSH YOURSELF TO YUR LIMITS ACHIVE YOUR FITNESS GOALS</p>

<article class="abs card" style="left:90px">
  <div class="card-photo" role="img" aria-label="Two trainers posing in athletic wear" style="background:linear-gradient(135deg,#2b3550,#1c2233 60%,#3a3f55)"></div>
  <div class="card-body"><h2 class="card-title">WHO WE ARE</h2><p class="card-text">Lorem ipsum dolor sit amet, consectetur adipiscing elit, sed do eiusmod tempor incididunt ut labore et dolore magna aliqua</p></div>
</article>

<article class="abs card" style="left:409px">
  <div class="card-photo framed" role="img" aria-label="Woman doing a sit-up exercise in a gym" style="background:linear-gradient(135deg,#cfcfcf,#8a8a8a 50%,#e0e0e0)"></div>
  <svg class="abs plus" width="68" height="68" viewBox="0 0 68 68"><circle cx="34" cy="34" r="33" fill="#d21f26" stroke="#fff" stroke-width="1.5"/><path d="M34 25v18M25 34h18" stroke="#fff" stroke-width="4"/></svg>
  <div class="card-body"><h2 class="card-title">OUR CLASSES</h2><p class="card-text">Lorem ipsum dolor sit amet, consectetur adipiscing elit, sed do eiusmod tempor incididunt ut labore et dolore magna aliqua</p></div>
</article>

<article class="abs card" style="left:727px">
  <div class="card-photo" role="img" aria-label="Man doing a dumbbell press on an incline bench in a gym" style="background:linear-gradient(135deg,#e6e6e6,#a9a9a9 55%,#d6d6d6)"></div>
  <div class="card-body"><h2 class="card-title">GALLERY</h2><p class="card-text">Lorem ipsum dolor sit amet, consectetur adipiscing elit, sed do eiusmod tempor incididunt ut labore et dolore magna aliqua</p></div>
</article>

<div class="abs arrows">
  <svg width="29" height="29" viewBox="0 0 29 29" fill="none" stroke="#fff" stroke-width="1.5"><circle cx="14.5" cy="14.5" r="13.5"/><path d="M20 14.5H9M13 10l-4.5 4.5L13 19"/></svg>
  <svg width="29" height="29" viewBox="0 0 29 29" fill="none" stroke="#fff" stroke-width="1.5"><circle cx="14.5" cy="14.5" r="13.5"/><path d="M9 14.5h11M16 10l4.5 4.5L16 19"/></svg>
</div>

<footer>
  <h3 class="abs f-head" style="left:73px">QUICK LINKS</h3>
  <ul class="abs links">
    <li class="active">Home</li><li>Gallery</li>
    <li>About Us</li><li>Blog</li>
    <li>The GYM</li><li>Contact Us</li>
    <li>The Bootcamp</li>
  </ul>

  <h3 class="abs f-head" style="left:388px">KEEP IN TOUCH</h3>
  <p class="abs touch-text">Lorem ipsum dolor sit amet, consectetur adipiscing elit, sed do</p>
  <div class="abs email-box">EMAIL ID
    <svg width="16" height="16" viewBox="0 0 24 24" fill="none" stroke="#8a8a8a" stroke-width="1.6"><path d="M22 2L2 10l8 3 3 8z M10 13L22 2"/></svg>
  </div>

  <h3 class="abs f-head" style="left:775px">OUR LOCATION</h3>
  <div class="abs loc">
    <div class="loc-row"><span class="loc-label">Address :</span><span>Lorem ipsum dolor sit,<br>consectetur adipiscing.</span></div>
    <div class="loc-row"><span class="loc-label">Contact :</span><span>123 555 0190</span></div>
    <div class="loc-row"><span class="loc-label">Email ID :</span><span>hello@ironbarktraininghub.com</span></div>
  </div>

  <div class="abs divider"></div>
  <p class="abs copyright">© <b>IRONBARK TRAINING HUB</b> - 2017. All Rights Reserved.</p>
  <div class="abs social"><span></span><span class="on"></span><span></span><span></span></div>
</footer>

</body>
</html>
```